Full Page Ad

We are like looking for something modern, Rustic and unique for a full page ad that includes our logo, office locations, contact information. Please see our webpage and www.BRINKClaimsworks.com. I can send our logo as well.
Updates

Looking for something elegant but industrial, rustic and modern. Added Sunday, June 4, 2017

Industry/Entity Type

Insurance

Font styles to use
Serif

Requirements
Must have
• Contact information

```html
<!DOCTYPE html>
<html lang="en">
<head>
<meta charset="utf-8">
<title>BRINK – When It Happens</title>
<link href="https://fonts.googleapis.com/css2?family=Lato:ital,wght@0,400;0,700;0,900;1,700&display=swap" rel="stylesheet">
<style>
  :root{
    --orange:#d67b3e;
    --orange-text:#d9783a;
    --white:#ffffff;
    --ink:#2a2522;
    --page-bg:#e6ebee;
    --wall-top:#c9d6de;
    --wall-mid:#b9c9d2;
    --water:#a3b3bc;
  }
  *{margin:0;padding:0;box-sizing:border-box}
  html,body{width:1200px;height:1200px;overflow:hidden;background:var(--page-bg)}
  body{font-family:"Lato",sans-serif;position:relative}
  .ad{position:absolute;left:197px;top:30px;width:806px;height:1140px;background:var(--white);box-shadow:0 6px 24px rgba(0,0,0,.18);overflow:hidden}
  .top-band{position:absolute;left:0;top:0;width:100%;height:69px;background:var(--orange);display:flex;align-items:center;justify-content:center;gap:18px;color:var(--white);font-weight:900;font-size:16px;letter-spacing:4px}
  .top-band .sep{font-weight:400;letter-spacing:0;opacity:.85}
  .scene{position:absolute;left:0;top:77px;width:100%;height:927px;background:linear-gradient(180deg,var(--wall-top) 0%,var(--wall-mid) 70%,var(--water) 100%)}
  .tagline{position:absolute;right:52px;top:118px;color:var(--orange-text);font-style:italic;font-weight:700;font-size:20px}
  .headline{position:absolute;left:122px;top:204px;color:var(--white);font-weight:900;font-size:68px;letter-spacing:-1px;line-height:1.2}
  .perils{position:absolute;left:122px;top:290px;color:var(--orange-text);font-weight:700;font-size:22px}
  .intro{position:absolute;left:207px;top:368px;width:340px;color:var(--white);font-size:15px;line-height:22px}
  .services h2{position:absolute;left:207px;top:514px;color:var(--orange-text);font-weight:900;font-size:22px;line-height:25px}
  .services p{position:absolute;left:207px;top:568px;width:370px;color:var(--white);font-size:14px;line-height:18px}
  .footer-rule{position:absolute;left:0;top:1004px;width:100%;height:10px;background:var(--white)}
  .footer{position:absolute;left:0;top:1016px;width:100%;height:124px;background:var(--orange);color:var(--white)}
  .brand{position:absolute;left:47px;top:26px}
  .brand .name{font-weight:900;font-size:47px;line-height:1;letter-spacing:1px}
  .brand .full{font-size:9px;margin-top:6px;letter-spacing:.3px}
  .divider{position:absolute;top:32px;width:2px;height:50px;background:var(--white)}
  .divider.one{left:256px}
  .divider.two{left:504px}
  .contact{position:absolute;left:270px;top:32px;font-size:11px;line-height:14px}
  .call{position:absolute;left:521px;top:28px;color:var(--ink);font-weight:900;font-size:29px;line-height:31px}
  .call .label{color:var(--white)}
</style>
</head>
<body>
  <main class="ad">
    <header class="top-band">
      <span>24/7 CLAIM SERVICE</span><span class="sep">|</span>
      <span>FAST REPORTING</span><span class="sep">|</span>
      <span>PREMIUM QUALITY</span>
    </header>

    <div class="scene" role="img" aria-label="Photo of a flooded living room: a grey sofa with cushions and a red throw and a potted tree standing in water against a pale blue wall"></div>

    <p class="tagline">Committed to satisfying your needs.</p>
    <h1 class="headline">When It Happens</h1>
    <p class="perils">Accidents, Disasters, Fire, Flood, Wind, Property &amp; Liability</p>

    <p class="intro">BRINK retains the benefits of a large firm in our capacity to handle high volume and complex claims over a large geographical area while at the same time retaining flexibility and personal tailored service.</p>

    <section class="services">
      <h2>Independent Claim<br>Adjusters &amp; Administration</h2>
      <p>With 12 locations throughout the North East we are able to service all of New York State as well as servicing Vermont, Western Massachusetts, Connecticut, Northern New Jersey and Pennsylvania.</p>
    </section>

    <div class="footer-rule"></div>
    <footer class="footer">
      <div class="brand">
        <div class="name">BRINK</div>
        <div class="full">BRINK REGIONAL CLAIMS SERVICES</div>
      </div>
      <div class="divider one"></div>
      <address class="contact" style="font-style:normal">
        Home Office: PO Box 215<br>
        410 Mill Ridge Road Harlow Falls, NY 12990<br>
        Phone: 518-555-0147 | Fax: 888-555-0182<br>
        www.brinkclaimsworks.com
      </address>
      <div class="divider two"></div>
      <div class="call"><span class="label">CALL</span><br>1-800-555-0163</div>
    </footer>
  </main>
</body>
</html>
```